Create Website for Brisk Renovations

*********** This contest is for the creation of a fully functional, multi-page website for our company. The web designer will be chosen through the contest mock-up presentation he or she will submit that will show the flowchart of page presentation and web design layout ***********

1. What we need: We need a website that makes customers feel comfortable and trust that we can do the bathroom renovation they have been wanting. Focusing on tile, marble, granite installation. Our focus also is hardwood floors (installation & refinishing). We expect that the site moves future customers to establish a first contact with us, due to that fact the site have to be professional and must reflect our main objective that is to inform that we can remodel bathrooms or work on their hardwood floors.
2. About us: We have been specializing in many facets of interior renovations for over 25 years. In 2008 we decided to get focus in hardwood floors only, for that reason we opened a small company dedicated to refinish and install hardwood flooring (www.OakvaleBoards.example), at the same time we kept doing complete renovation projects for our previous clients. Now, being sure that we have enough experience to do it, we want to expand our company’s focus to perform bathroom remodeling in addition to hardwood flooring. The new company name is BRISK RENOVATIONS and will be specialized in all home improvement disciplines such us bathroom remodeling, interior finishes, ceramic, granite, marble, and wood flooring.
3. What we are looking from the web designer: The web designer must present an original design that shows that he made an evaluation of our needs.
You will be responsible for the design and graphic presentation of all the pages that builds up the web site. (We will take care finding a content writer, however you must work in close collaboration). The home improvement market in the U.S. is huge, there is a lot of competition. We want a webpage that appeals to the real decision maker of the household, the woman. Our web designer has to display a keen ability in knowing how to appeal to the decision maker.
4) Awarding process: A mockup of the "home page" would be good to see if you are the right one to be chose. However, along with the mockup, the designer must provide a complete scheme of the web site, that means that you will need to present how many pages a web site of this kind needs, also you should indicate the elements that will go on each page. We will select the most suitable designer for the job.
5) What we provide. We will include as a reference our new business card logo and the previous site that we only had for wooden floors. www.oakvaleboards.example) along with a brochure we had produced. We currently have a space saver with www.briskrenovations.example

```html
<!DOCTYPE html>
<html lang="en">
<head>
<meta charset="utf-8">
<title>Flooring Types – Brisk Renovations</title>
<link href="https://fonts.googleapis.com/css2?family=Open+Sans:wght@300;400;600;700&display=swap" rel="stylesheet">
<style>
:root{
  --dark:#2b2e37;
  --footer:#262833;
  --accent:#29a9d6;
  --text:#333;
  --muted:#777;
  --light:#f1f1f1;
  --line:#e4e4e4;
  --wood-dark:#8a4a1c;
  --wood-mid:#c07a3e;
  --wood-light:#e4b27a;
}
*{box-sizing:border-box;margin:0;padding:0}
html,body{width:1049px;height:1200px;overflow:hidden;background:#fff}
body{font-family:"Open Sans",Arial,sans-serif;color:var(--text)}
.page{position:relative;width:900px;height:1030px;transform:scale(1.1656);transform-origin:0 0}
.abs{position:absolute}

/* top bar */
.topbar{left:0;top:0;width:900px;height:30px;background:var(--dark);color:#fff;font-size:10px}
.topbar .icon{top:7px;width:16px;height:16px;background:#fff;border-radius:2px}
.topbar .txt{top:8px}
.topbar .follow{left:644px;top:9px;color:#9a9ca3;font-size:9.5px}
.topbar .social{top:0;width:31px;height:30px;border-left:1px solid #3c3f48}
.topbar .social span{position:absolute;left:11px;top:10px;width:10px;height:10px;border-radius:50%;background:#c9cacd}

/* header */
.header{left:0;top:30px;width:900px;height:65px;background:#fff}
.brand{left:107px;top:48px;font-size:15px;font-weight:700;color:var(--dark);letter-spacing:.5px;line-height:18px}
.brand-mark{left:107px;top:36px;width:12px;height:12px;border-radius:50%;background:var(--accent)}
.nav{top:57px;font-size:9.5px;color:#222;white-space:nowrap}
.nav.active{color:var(--accent)}
.nav .caret{font-size:6px;color:#aaa;margin-left:2px;vertical-align:1px}
.nav.active .caret{color:var(--accent)}
.nav-line{left:416px;top:92px;width:55px;height:2px;background:var(--accent)}

/* title band */
.titleband{left:0;top:95px;width:900px;height:67px;background:linear-gradient(180deg,#e9e9e9,#f2f2f2)}
.titleband h1{position:absolute;left:103px;top:20px;font-size:19px;font-weight:300;color:#333;letter-spacing:.2px}

/* sidebar */
.sidemenu{left:77px;top:225px;width:171px;height:126px;border:1px solid var(--line)}
.sidemenu li{list-style:none;position:absolute;left:12px;width:145px;font-size:10.5px;color:var(--muted);padding-left:14px;line-height:14px}
.sidemenu li::before{content:"";position:absolute;left:0;top:4px;border-left:4px solid #777;border-top:3px solid transparent;border-bottom:3px solid transparent}
.sidemenu li.current{color:var(--accent)}
.sidemenu li.current::before{border-left-color:var(--accent)}
.sidemenu .sep{position:absolute;left:12px;width:145px;height:1px;background:var(--line)}
.side-h{left:77px;font-size:13.5px;color:#222}
.brochure{left:77px;width:171px;height:52px;background:var(--light)}
.brochure .file{position:absolute;left:14px;top:17px;width:12px;height:16px;background:#9a9a9a;border-radius:1px}
.brochure b{position:absolute;left:36px;top:12px;font-size:11px;font-weight:600;color:#222}
.brochure small{position:absolute;left:36px;top:29px;font-size:9.5px;color:#999}
.askbox{left:77px;top:575px;width:171px;height:120px;border:1px solid var(--line)}
.askbox p{position:absolute;left:10px;top:18px;width:150px;font-size:9.5px;line-height:18.5px;color:var(--muted)}
.askbox .btn{position:absolute;left:48px;top:79px;width:74px;height:25px;background:var(--light);border:1px solid #ddd;font-size:9.5px;color:#444;text-align:center;line-height:23px}

/* content */
.content-h{left:268px;top:212px;font-size:20px;font-weight:600;color:#222}
.content-rule{left:268px;top:247px;width:53px;height:1px;background:var(--accent)}
.para{left:268px;width:560px;font-size:9.3px;line-height:15px;color:#333}
.sub-h{left:268px;top:359px;font-size:14px;color:#222}
.floor{top:402px;width:166px;height:166px}
.floor .photo{position:absolute;inset:0;border-radius:50%;border:1px solid #e6e6e6}
.floor .label{position:absolute;left:-10px;top:123px;width:186px;height:31px;background:#fff;font-size:10px;color:#555;text-align:center;line-height:31px;white-space:nowrap}
.wood1{background:linear-gradient(150deg,var(--wood-dark),var(--wood-mid) 45%,#a45a25)}
.wood2{background:linear-gradient(160deg,#f4f0ea 0%,#b8743d 40%,#d9b992 70%,#f2eee8)}
.wood3{background:linear-gradient(135deg,var(--wood-mid),var(--wood-light) 50%,#c86e34)}

/* footer */
.footer{left:0;top:785px;width:900px;height:245px;background:var(--footer);color:#8b8d95}
.footer h4{position:absolute;top:43px;font-size:9.5px;font-weight:700;color:#fff;letter-spacing:.8px}
.footer .about{position:absolute;left:103px;top:68px;width:220px;font-size:9.5px;line-height:15px}
.footer .loc{position:absolute;left:341px;top:68px;font-size:9.5px;line-height:18px}
.footer .loc b{color:#fff;font-weight:600}
.footer .loc .w{color:#fff}
.footer .dot{position:absolute;top:71px;width:13px;height:13px;border-radius:50%;background:#5a5d66}
.footer .subscribe{position:absolute;left:579px;top:104px;width:191px;height:24px;background:#30323d;font-size:9px;color:#5d606a;padding:6px 8px}
.footer .send{position:absolute;left:770px;top:104px;width:27px;height:24px;background:var(--accent)}
.footer .send span{position:absolute;left:9px;top:9px;width:9px;height:6px;background:#fff}
.footer .note{position:absolute;left:579px;top:136px;font-size:7.5px;font-style:italic;color:#666}
.footer .bottom{position:absolute;top:213px;font-size:10px;color:#ccc}
.footer .copy{position:absolute;right:103px;top:213px;font-size:10px;color:#aaa}
.footer .edge{position:absolute;left:0;top:242px;width:900px;height:3px;background:var(--accent)}
</style>
</head>
<body>
<div class="page">

  <div class="abs topbar">
    <svg class="abs icon" style="left:103px" viewBox="0 0 16 16"><path d="M5 3.5l1.8 2.3-1 1.2c.6 1.3 1.8 2.5 3.2 3.2l1.2-1 2.3 1.8-1 1.6C8 12.4 3.6 8 3.4 4.5z" fill="#2b2e37"/></svg>
    <span class="abs txt" style="left:128px">914-555-0182</span>
    <svg class="abs icon" style="left:201px" viewBox="0 0 16 16"><rect x="3" y="4.5" width="10" height="7" fill="#2b2e37"/><path d="M3 4.5l5 4 5-4" stroke="#fff" fill="none"/></svg>
    <span class="abs txt" style="left:224px">hello@briskrenovations.example</span>
    <span class="abs follow">Follow Us:</span>
    <div class="abs social" style="left:701px"><span></span></div>
    <div class="abs social" style="left:732px"><span></span></div>
    <div class="abs social" style="left:763px;border-right:1px solid #3c3f48"><span></span></div>
  </div>

  <div class="abs header"></div>
  <div class="abs brand-mark"></div>
  <div class="abs brand">BRISK<br>RENOVATIONS</div>
  <span class="abs nav" style="left:308px">Home</span>
  <span class="abs nav" style="left:355px">Projects<span class="caret">▼</span></span>
  <span class="abs nav active" style="left:416px">Our Services<span class="caret">▼</span></span>
  <span class="abs nav" style="left:497px">About us</span>
  <span class="abs nav" style="left:556px">Offers</span>
  <span class="abs nav" style="left:603px">Info</span>
  <span class="abs nav" style="left:641px">Testimonials</span>
  <span class="abs nav" style="left:715px">FAQ</span>
  <span class="abs nav" style="left:753px">Contact</span>
  <div class="abs nav-line"></div>

  <div class="abs titleband"><h1>FLOORING TYPES</h1></div>

  <ul class="abs sidemenu">
    <li style="top:12px">Floor Installation Type</li>
    <div class="sep" style="top:35px"></div>
    <li class="current" style="top:48px">Flooring types</li>
    <div class="sep" style="top:71px"></div>
    <li style="top:85px">Hardwood Choosing Factors</li>
  </ul>

  <div class="abs side-h" style="top:381px">Our Brochures</div>
  <div class="abs brochure" style="top:410px"><span class="file"></span><b>Research Results</b><small>Download.pdf</small></div>
  <div class="abs brochure" style="top:469px"><span class="file"></span><b>Material Engineering</b><small>Download.txt</small></div>

  <div class="abs side-h" style="top:550px">Questions? Budgets?</div>
  <div class="abs askbox">
    <p>If you want to recieve more information to make your choice, we will be happy to help you.</p>
    <div class="btn">Contact Now</div>
  </div>

  <div class="abs content-h">Flooring types</div>
  <div class="abs content-rule"></div>
  <p class="abs para" style="top:272px">Hardwood floors are an investment that will last for a long time with the proper installation and care. There are different modes of installation for engineered wood strips, solid wood strips, and parquet.</p>
  <p class="abs para" style="top:315px">With all modes of installation moisture testing is imperative to ensure proper installation. Installation can be a painstaking process but we take pride in leaving your home looking as beautiful as we found it.</p>
  <div class="abs sub-h">See and compare each type of floor:</div>

  <div class="abs floor" style="left:278px"><div class="photo wood1" role="img" aria-label="Photo of solid hardwood planks"></div><div class="label">Solid hardwood floor</div></div>
  <div class="abs floor" style="left:463px"><div class="photo wood2" role="img" aria-label="Photo of stacked engineered hardwood boards"></div><div class="label">Engineered solid hardwood</div></div>
  <div class="abs floor" style="left:648px"><div class="photo wood3" role="img" aria-label="Photo of laminate flooring planks"></div><div class="label">Laminate flooring</div></div>

  <footer class="abs footer">
    <h4 style="left:103px">ABOUT BRISK RENOVATIONS</h4>
    <p class="about">Temporibus autem quibusdam et aut officiis debitis aut rerum necessitatibus saepe eveniet ut et voluptates repudiandae sint et molestiae non recusandae itaque earum rerum.</p>
    <h4 style="left:341px">LOCATION</h4>
    <div class="loc">Millbrook, New York, United States<br><b>P:</b> (914) 555-0182<br><b>E:</b> <span class="w">hello@briskrenovations.example</span><br><b>Mon-Fri:</b> 9:00 am – 5:00 pm<br><b>Sat &amp; Sun:</b> closed</div>
    <h4 style="left:579px">FOLLOW US</h4>
    <span class="dot" style="left:580px"></span>
    <span class="dot" style="left:604px"></span>
    <span class="dot" style="left:628px"></span>
    <div class="subscribe">Enter e-mail for subscribe</div>
    <div class="send"><span></span></div>
    <div class="note">We promise not to send you spam</div>
    <span class="bottom" style="left:113px">Help</span>
    <span class="bottom" style="left:153px">Privacy</span>
    <span class="bottom" style="left:204px">Terms</span>
    <span class="copy">© 2017. «Brisk Renovations».</span>
    <div class="edge"></div>
  </footer>

</div>
</body>
</html>
```